Trinket Crate Guild - New Website Design

Create a professional website for charms of the month club; a subscription box business. the website URL will be www.TrinketCrateGuild.com
Please see ruffleparcel.com; fudgeguild.com and pupcrate.com for the concept I am after. The business has not been launched yet, I am currently in the pre-launch stage using a specialized landing page website, and so the time scale for developing my professional looking website is up to 1-2 weeks.
The webpage should have a fun feel and should match the style of the company logo at fudgeguild.com or pupcrate.com. The pages to include are 'Home', 'About us' and 'Get Started'
Thank you and good luck!

```html
<!DOCTYPE html>
<html lang="en">
<head>
<meta charset="utf-8">
<title>Trinket Crate Guild</title>
<link rel="stylesheet" href="https://fonts.googleapis.com/css2?family=Oswald:wght@400;500;700&family=Nunito:wght@300;400;600&family=Open+Sans:wght@400;600&display=swap">
<style>
:root{
  --ink:#222226;
  --text:#444449;
  --muted:#8a8a90;
  --pink:#e8799a;
  --pink-soft:#f3b4c6;
  --pink-line:#e9a3b4;
  --rose-red:#e0425a;
  --hero-bg:#f5f3f4;
  --plan-bg:#fcf1f3;
  --white:#ffffff;
}
*{box-sizing:border-box;margin:0;padding:0}
html,body{width:1200px;height:2913px;overflow:hidden;background:var(--white)}
body{position:relative;font-family:"Open Sans",sans-serif;color:var(--text)}

/* header */
.site-header{position:absolute;left:0;top:0;width:1200px;height:157px;background:var(--white);border-bottom:2px solid #ececee}
.brand{position:absolute;top:24px;left:0;width:1200px;text-align:center;font-family:"Oswald",sans-serif;font-weight:700;font-size:34px;letter-spacing:1px;color:var(--ink)}
.main-nav a{position:absolute;top:97px;height:28px;line-height:28px;font-family:"Nunito",sans-serif;font-size:16px;color:var(--ink);text-decoration:none;transform:translateX(-50%);white-space:nowrap}
.main-nav a.active{background:var(--pink);color:var(--white);border-radius:14px;width:89px;text-align:center}

/* hero */
.hero{position:absolute;left:0;top:159px;width:1200px;height:860px;background:linear-gradient(to bottom,var(--hero-bg) 0,var(--hero-bg) 600px,var(--white) 860px)}
.hero-floral{position:absolute;left:233px;top:165px;width:622px;height:592px;border-radius:50%;background:radial-gradient(ellipse at center,rgba(240,180,195,.55) 0%,rgba(236,196,200,.35) 45%,rgba(220,225,200,.25) 65%,rgba(245,243,244,0) 75%)}
.hero-card{position:absolute;left:369px;top:227px;width:462px;height:437px;background:var(--white);box-shadow:0 6px 22px rgba(0,0,0,.14);z-index:1}
.hero-card .frame{position:absolute;left:17px;top:16px;width:428px;height:400px;border:3px solid var(--pink)}
.hero-card .product{position:absolute;left:95px;top:45px;width:270px;height:330px;border-radius:40%;background:radial-gradient(ellipse at center,#6c7088 0%,#9aa0b4 40%,#d9dbe2 70%,#ffffff 90%)}
.hero-word{position:absolute;z-index:2;font-family:"Oswald",sans-serif;font-weight:500;font-size:98px;line-height:1;color:var(--ink);letter-spacing:-1px;white-space:nowrap}
.hero-word.one{left:14px;width:404px;text-align:right;top:282px}
.hero-word.two{left:645px;top:500px}

.welcome-title{position:absolute;top:798px;left:0;width:1200px;text-align:center;font-family:"Nunito",sans-serif;font-weight:300;font-size:34px;color:var(--ink)}
.welcome-copy{position:absolute;top:855px;left:132px;width:936px;text-align:justify;font-size:13.5px;line-height:20px;color:var(--text)}

/* how it works */
.section-title{position:absolute;left:0;width:1200px;text-align:center;font-family:"Nunito",sans-serif;font-weight:300;font-size:34px;color:var(--ink)}
.steps-line{position:absolute;left:272px;top:1198px;width:656px;height:2px;background:var(--pink-line)}
.step-circle{position:absolute;top:1145px;width:106px;height:106px;margin-left:-53px;border-radius:50%;border:2px solid var(--pink-line);background:var(--white);text-align:center;line-height:102px;font-family:"Nunito",sans-serif;font-weight:300;font-size:38px;color:var(--rose-red)}
.step-title{position:absolute;top:1274px;width:320px;margin-left:-160px;text-align:center;font-family:"Nunito",sans-serif;font-weight:400;font-size:18px;color:var(--ink)}
.step-copy{position:absolute;top:1308px;width:290px;margin-left:-145px;text-align:center;font-size:12.5px;line-height:20px;color:var(--muted)}
.step-link{position:absolute;top:1358px;width:200px;margin-left:-100px;text-align:center;font-size:13px;color:var(--pink)}

/* plans */
.plans{position:absolute;left:0;top:1486px;width:1200px;height:584px;background:var(--plan-bg)}
.plan-card{position:absolute;top:1631px;width:265px;height:335px;background:var(--white);border-radius:28px;box-shadow:0 3px 12px rgba(0,0,0,.22)}
.plan-card .visual{position:absolute;left:65px;top:22px;width:135px;height:120px;border-radius:14px}
.plan-card h3{position:absolute;top:165px;width:100%;text-align:center;font-family:"Nunito",sans-serif;font-weight:400;font-size:23px;color:var(--ink)}
.plan-card .price{position:absolute;top:198px;width:100%;text-align:center;font-family:"Nunito",sans-serif;font-size:21px;color:var(--rose-red)}
.plan-card .note{position:absolute;top:227px;width:100%;text-align:center;font-size:12px;color:var(--text)}
.plan-card .cta{position:absolute;left:61px;top:264px;width:144px;height:34px;line-height:34px;border-radius:17px;background:var(--pink);color:var(--white);text-align:center;font-family:"Nunito",sans-serif;font-size:17px}

/* subscription */
.subscribe{position:absolute;left:0;top:2070px;width:1200px;height:625px;background:var(--white)}
.subscribe-floral{position:absolute;left:0;top:2100px;width:1200px;height:570px;background:radial-gradient(ellipse 60% 45% at 50% 20%,rgba(243,200,210,.45),rgba(255,255,255,0) 70%),radial-gradient(ellipse 25% 40% at 3% 60%,rgba(240,190,205,.45),rgba(255,255,255,0) 80%),radial-gradient(ellipse 25% 40% at 97% 60%,rgba(240,190,205,.45),rgba(255,255,255,0) 80%),radial-gradient(ellipse 50% 25% at 50% 95%,rgba(225,230,205,.4),rgba(255,255,255,0) 80%)}
.subscribe-card{position:absolute;left:151px;top:2249px;width:898px;height:295px;background:var(--white);box-shadow:0 3px 14px rgba(0,0,0,.12)}
.subscribe-card .frame{position:absolute;left:26px;top:19px;width:846px;height:253px;border:2px solid var(--pink-line)}
.subscribe-charm{position:absolute;left:509px;top:2214px;width:163px;height:97px;border-radius:50%;background:radial-gradient(ellipse at center,rgba(255,255,255,0) 30%,#3c63b8 38%,#7ea0dd 50%,rgba(255,255,255,0) 62%)}
.subscribe-title{position:absolute;top:2325px;left:0;width:1200px;text-align:center;font-family:"Nunito",sans-serif;font-weight:400;font-size:34px;color:var(--ink)}
.subscribe-sub{position:absolute;top:2371px;left:0;width:1200px;text-align:center;font-size:14px;color:var(--text)}
.email-field{position:absolute;left:350px;top:2416px;width:499px;height:50px;border:1.5px solid #b9b9bd;border-radius:25px;background:var(--white);overflow:hidden}
.email-field .placeholder{position:absolute;left:24px;top:0;line-height:47px;font-size:14px;color:var(--text)}
.email-field .submit{position:absolute;right:0;top:0;width:84px;height:100%;background:var(--pink);color:var(--white);text-align:center;line-height:47px;font-size:14px}

/* footer */
.site-footer{position:absolute;left:0;top:2695px;width:1200px;height:218px;background:linear-gradient(to bottom,#f2b3c6,#e47799)}
.footer-links{position:absolute;top:82px;left:0;width:1200px;text-align:center;font-size:12px;font-weight:600;color:var(--white);letter-spacing:.3px;word-spacing:4px}
.social{position:absolute;top:116px;left:500px;width:200px;height:30px}
.footer-copy{position:absolute;top:155px;left:0;width:1200px;text-align:center;font-size:12px;color:var(--white)}
</style>
</head>
<body>

<header class="site-header">
  <div class="brand">TRINKET CRATE GUILD</div>
  <nav class="main-nav">
    <a class="active" style="left:248px">HOME</a>
    <a style="left:381px">ABOUT US</a>
    <a style="left:528px">PRODUCTS</a>
    <a style="left:662px">BLOG</a>
    <a style="left:794px">SUBSCRIBE</a>
    <a style="left:940px">CONTACT</a>
  </nav>
</header>

<section class="hero"></section>
<div class="hero-floral" role="img" aria-label="Watercolour wreath of pink magnolia blossoms and green leaves"></div>
<div class="hero-card">
  <div class="frame"></div>
  <div class="product" role="img" aria-label="Silver chain bracelet with blue and grey beads and charms"></div>
</div>
<div class="hero-word one">TRINKET</div>
<div class="hero-word two">CRATEGUILD</div>

<h1 class="welcome-title">WELCOME TO TRINKETCRATEGUILD</h1>
<p class="welcome-copy">It is a long established fact that a reader will be distracted by the readable content of a page when looking at its layout. The point of using Lorem Ipsum is that it has a more-or-less normal distribution of letters, as opposed to using 'Content here, content here', making it look like readable English. Many desktop publishing packages and web page editors now use Lorem Ipsum as their default model text,</p>

<h2 class="section-title" style="top:1070px">HOW IT WORKS</h2>
<div class="steps-line"></div>
<div class="step-circle" style="left:272px">1</div>
<div class="step-circle" style="left:602px">2</div>
<div class="step-circle" style="left:928px">3</div>
<h3 class="step-title" style="left:276px">DISCOVER DELICIOUSNESS</h3>
<h3 class="step-title" style="left:602px">YOUR PERFECT BOX</h3>
<h3 class="step-title" style="left:930px">ENTERCHARM HEAVEN</h3>
<p class="step-copy" style="left:276px">It has survived not only five centuries, but also the leap into electronic typesetting,</p>
<p class="step-copy" style="left:604px">It has survived not only five centuries, but also the leap into electronic typesetting,</p>
<p class="step-copy" style="left:930px">It has survived not only five centuries, but also the leap into electronic typesetting,</p>
<div class="step-link" style="left:276px">Learn More -&gt;</div>
<div class="step-link" style="left:604px">Learn More -&gt;</div>
<div class="step-link" style="left:930px">Learn More -&gt;</div>

<section class="plans"></section>
<h2 class="section-title" style="top:1538px">CHOOSE A PLAN</h2>

<div class="plan-card" style="left:153px">
  <div class="visual" role="img" aria-label="Wooden treasure chest overflowing with pearls and gold jewellery" style="background:radial-gradient(ellipse at center,#8a5a30 0%,#c9a56a 45%,#f3ece0 75%,#ffffff 90%)"></div>
  <h3>Monthly Plan</h3>
  <div class="price">$29.99/month</div>
  <div class="note">(plus shipping)</div>
  <div class="cta">Get started</div>
</div>
<div class="plan-card" style="left:472px">
  <div class="visual" role="img" aria-label="Open black ring box holding a green gemstone ring" style="background:radial-gradient(ellipse at center,#1e1e22 0%,#3a3a40 40%,#e6e6e8 72%,#ffffff 88%)"></div>
  <h3>6 Month Plan</h3>
  <div class="price">$24.99/month</div>
  <div class="note">(plus shipping)</div>
  <div class="cta">Get started</div>
</div>
<div class="plan-card" style="left:794px">
  <div class="visual" role="img" aria-label="Red lacquered jewellery box with gold trim" style="background:radial-gradient(ellipse at center,#b21f2e 0%,#c84a4a 40%,#f1dcdc 72%,#ffffff 88%)"></div>
  <h3>12 Month Plan</h3>
  <div class="price">$21.99/month</div>
  <div class="note">(plus shipping)</div>
  <div class="cta">Get started</div>
</div>

<section class="subscribe"></section>
<div class="subscribe-floral" role="img" aria-label="Soft watercolour border of pink magnolia branches"></div>
<div class="subscribe-card"><div class="frame"></div></div>
<div class="subscribe-charm" role="img" aria-label="Blue beaded charm bracelet"></div>
<h2 class="subscribe-title">SUBSCRIPTION</h2>
<p class="subscribe-sub">It has survived not only five centuries,</p>
<div class="email-field">
  <span class="placeholder">Email id</span>
  <span class="submit">Submit</span>
</div>

<footer class="site-footer">
  <div class="footer-links">ABOUT &nbsp;|&nbsp; PRIVACY &nbsp;|&nbsp; TERMS &nbsp;|&nbsp; LEGAL &nbsp;|&nbsp; CONTACT</div>
  <svg class="social" viewBox="0 0 200 30" aria-label="Social links">
    <g fill="none" stroke="#ffffff" stroke-width="1.5">
      <circle cx="15" cy="15" r="12"/>
      <circle cx="49" cy="15" r="12"/>
      <circle cx="83" cy="15" r="12"/>
      <circle cx="117" cy="15" r="12"/>
      <circle cx="151" cy="15" r="12"/>
      <circle cx="185" cy="15" r="12"/>
    </g>
  </svg>
  <div class="footer-copy">Copyright © 2017 &nbsp;All Rights Reserved</div>
</footer>

</body>
</html>
```